Kip Video Games

I need a design for a campaign game, pure news no sale, it fun and modern, and also something different and do it to the other pages there, the design must convey the central idea of ​​the page. You should be able to get on the platform wordpress

Industry/Entity Type

Games

Number of Pages Required

1 page

Font styles to use
Sans Serif

```html
<!DOCTYPE html>
<html lang="en">
<head>
<meta charset="utf-8">
<title>Kip Video Games</title>
<link rel="stylesheet" href="https://fonts.googleapis.com/css2?family=Roboto:wght@400;500;700&family=Open+Sans:wght@400;600&family=Noto+Serif:wght@400&display=swap">
<style>
:root{
  --red:#d3262b;
  --ink:#222;
  --text:#6b6b6b;
  --muted:#9a9a9a;
  --line:#e2e2e2;
  --page:#ffffff;
  --footer:#1c1c1c;
  --footer-bottom:#0d0d0d;
}
*{box-sizing:border-box;margin:0;padding:0}
html,body{width:1200px;height:3147px;overflow:hidden;background:var(--page)}
body{position:relative;font-family:"Open Sans",Arial,sans-serif;color:var(--text)}
.abs{position:absolute}
.ph{position:absolute;display:block}

/* header */
.brand{left:30px;top:54px;display:flex;align-items:center;gap:14px}
.brand-mark{width:62px;height:62px;background:var(--red);border-radius:50%}
.brand-name{font-family:"Roboto",sans-serif;font-weight:700;font-size:40px;color:var(--ink);letter-spacing:-0.5px}
.search{left:728px;top:52px;width:227px;height:40px;background:#e4e4e4;font-size:15px;color:#999;padding:10px 20px;display:flex;justify-content:space-between}
.social-top{left:996px;top:50px;display:flex;gap:7px}
.social-top span{width:38px;height:38px;border-radius:50%;background:#7a7a7a}
.nav{left:535px;top:134px;width:633px;display:flex;justify-content:space-between;align-items:center;font-family:"Noto Serif",Georgia,serif;font-size:16px;color:var(--ink)}
.nav .dot{width:5px;height:5px;border-radius:50%;background:#bbb}
.nav .active{color:var(--red)}

/* hero */
.hero{left:30px;top:193px;width:677px;height:474px;background:linear-gradient(160deg,#3d5a6b,#1f2f3a 60%,#111a20)}
.hero-caption{left:30px;top:538px;width:677px;height:129px;background:rgba(0,0,0,.45);padding:20px 40px}
.hero-caption h2{font-family:"Roboto",sans-serif;font-weight:400;font-size:30px;color:#fff}
.hero-caption p{font-size:12px;color:#ccc;width:520px;line-height:16px;margin-top:10px}
.arrow{width:30px;height:30px;background:var(--red);top:505px}
.side-shot{left:718px;width:450px;height:231px}
.shot-a{top:193px;background:linear-gradient(150deg,#6b5a44,#3a2f25 60%,#1a1613)}
.shot-b{top:436px;background:linear-gradient(160deg,#8a9099,#4b525a 60%,#22262b)}
.date-box{width:52px;height:52px;background:rgba(0,0,0,.55);color:#fff;text-align:center;font-family:"Roboto",sans-serif;font-size:18px;line-height:20px;padding-top:7px}
.date-box small{display:block;font-size:11px}
.zoom{width:52px;height:52px;background:var(--red)}

/* welcome */
.welcome{left:30px;top:708px;width:630px}
.welcome h1{font-family:"Roboto",sans-serif;font-weight:500;font-size:28px;color:var(--ink)}
.welcome p{font-size:12.5px;line-height:18px;margin-top:14px}

/* posts */
.post{left:30px;width:630px;height:330px}
.post .day{font-family:"Roboto",sans-serif;font-size:16px;color:var(--ink);font-weight:500}
.post .thumb{left:0;top:25px;width:226px;height:227px;background:radial-gradient(circle at 50% 65%,#c2321f,#4a0e08 60%,#0c0404)}
.post .body{left:251px;top:45px;width:370px}
.post h3{font-family:"Open Sans",sans-serif;font-weight:600;font-size:14.5px;line-height:21px;color:var(--red)}
.post p{font-size:12px;line-height:17px;margin-top:8px}
.tags{display:grid;grid-template-columns:128px 122px 110px;font-size:12px;row-gap:6px;margin-top:16px}
.byline{left:0;top:268px;font-size:10px;color:#555}
.byline b{color:var(--red);font-weight:400;margin-left:18px}

/* sidebar */
.side-head{left:718px;width:450px;height:65px;background:linear-gradient(#3e3e3e,#0d0d0d);color:#fff;font-family:"Roboto",sans-serif;font-weight:500;font-size:24px;padding:16px 38px}
.side-item{left:718px;width:450px;height:105px;border-bottom:1px solid var(--line)}
.side-item .pic{left:0;top:0;width:105px;height:105px}
.pic-knight{background:linear-gradient(#8c8c84,#4d4f4a)}
.pic-cube{background:#b3201c}
.side-item .txt{left:128px;top:14px;width:260px}
.side-item h4{font-family:"Roboto",sans-serif;font-weight:500;font-size:18px;color:var(--ink)}
.side-item p{font-size:12px;line-height:16px;margin-top:8px}
.side-item .meta{font-size:11px;color:#aaa;margin-top:6px;word-spacing:2px}
.more{left:718px;font-size:13px;color:var(--red)}
.comment{left:718px;width:450px;border-bottom:1px solid var(--line);padding:0 25px 16px}
.comment p{font-size:12px;line-height:16px}
.comment time{display:block;font-size:9px;color:#333;margin-top:8px;font-weight:600}
.recent{left:742px;top:1222px;font-family:"Roboto",sans-serif;font-weight:500;font-size:18px;color:var(--ink)}

/* banner */
.banner{left:0;top:1985px;width:1200px;height:409px;background:radial-gradient(ellipse at 60% 40%,#3c5580,#16254a 60%,#0b1530)}
.banner-text{left:109px;top:2118px;width:560px;color:#fff}
.banner-text h2{font-family:"Roboto",sans-serif;font-weight:400;font-size:30px}
.banner-text p{font-size:13px;line-height:19px;margin-top:14px;width:460px}
.btn{display:inline-block;margin-top:20px;background:var(--red);color:#fff;font-size:11px;padding:6px 22px}

/* testimonial */
.testimonial{left:0;top:2394px;width:1200px;height:361px;background:#f7f7f7}
.quote-mark{font-family:"Noto Serif",serif;font-size:60px;color:#e8e8e8}
.avatar{left:131px;top:2509px;width:152px;height:152px;border-radius:50%;border:3px solid #ddd;background:linear-gradient(#d7b08e,#b08466)}
.testimonial-text{left:304px;top:2526px;width:740px}
.testimonial-text p{font-size:15px;line-height:22px}
.testimonial-text cite{display:block;font-style:normal;font-family:"Roboto",sans-serif;font-weight:500;font-size:20px;color:var(--red);margin-top:12px}

/* footer */
.footer{left:0;top:2755px;width:1200px;height:321px;background:var(--footer);color:#fff}
.col{top:68px}
.col h5{font-family:"Roboto",sans-serif;font-weight:500;font-size:22px;margin-bottom:22px}
.col li{list-style:none;font-family:"Roboto",sans-serif;font-size:16px;line-height:29px}
.contact p{font-family:"Roboto",sans-serif;font-size:16px;line-height:22px}
.contact .phone{font-size:24px;margin-top:8px;line-height:30px}
.field{width:198px;height:32px;background:#333;font-size:11px;color:#888;padding:8px 12px;margin-bottom:10px}
.subscribe{margin-left:120px;width:78px;height:26px;background:var(--red);font-size:12px;text-align:center;line-height:26px}
.social-foot{display:flex;gap:18px}
.social-foot span{width:34px;height:34px;border-radius:50%;background:#fff}
.copyright{left:0;top:3076px;width:1200px;height:71px;background:var(--footer-bottom);color:#fff;font-family:"Roboto",sans-serif;font-size:17px;padding:24px 48px}
</style>
</head>
<body>

<header>
  <div class="abs brand"><span class="brand-mark"></span><span class="brand-name">Kip Video Games</span></div>
  <div class="abs search"><span>Search</span>
    <svg width="20" height="20" viewBox="0 0 20 20"><circle cx="8" cy="8" r="6" fill="none" stroke="#999" stroke-width="2"/><line x1="12.5" y1="12.5" x2="18" y2="18" stroke="#999" stroke-width="2"/></svg>
  </div>
  <div class="abs social-top"><span></span><span></span><span></span><span></span></div>
  <nav class="abs nav">
    <span>Home</span><i class="dot"></i><span class="active">Reviews</span><i class="dot"></i><span>Gallery</span><i class="dot"></i><span>Blog</span><i class="dot"></i><span>News &amp; Info</span><i class="dot"></i><span>Contact Us</span>
  </nav>
</header>

<section>
  <div class="ph hero" role="img" aria-label="Armored space soldiers with rifles on an alien battlefield"></div>
  <div class="abs hero-caption">
    <h2>Lorem Ipsum is simply dummy.</h2>
    <p>Lorem Ipsum is simply dummy text of the printing industry. An unknown printer took a galley of type and scrambled it to make a type specimen book.</p>
  </div>
  <div class="abs arrow" style="left:30px"><svg width="30" height="30"><path d="M18 9l-6 6 6 6" fill="none" stroke="#fff" stroke-width="2.5"/></svg></div>
  <div class="abs arrow" style="left:677px"><svg width="30" height="30"><path d="M12 9l6 6-6 6" fill="none" stroke="#fff" stroke-width="2.5"/></svg></div>

  <div class="ph side-shot shot-a" role="img" aria-label="Soldiers advancing through a burning battlefield"></div>
  <div class="abs date-box" style="left:1064px;top:365px">13<small>Mar</small></div>
  <div class="abs zoom" style="left:1116px;top:365px"><svg width="52" height="52"><circle cx="23" cy="23" r="9" fill="none" stroke="#fff" stroke-width="3"/><line x1="30" y1="30" x2="37" y2="37" stroke="#fff" stroke-width="3"/></svg></div>
  <div class="ph side-shot shot-b" role="img" aria-label="Soldier in a ruined city with helicopters overhead"></div>
  <div class="abs date-box" style="left:1064px;top:608px">22<small>Apr</small></div>
  <div class="abs zoom" style="left:1116px;top:608px"><svg width="52" height="52"><circle cx="23" cy="23" r="9" fill="none" stroke="#fff" stroke-width="3"/><line x1="30" y1="30" x2="37" y2="37" stroke="#fff" stroke-width="3"/></svg></div>
</section>

<main>
  <div class="abs welcome">
    <h1>WELCOME TO KIP VIDEO GAMES.</h1>
    <p>Lorem Ipsum is simply dummy text of the printing and typesetting industry. Lorem Ipsum has been the industry's standard dummy text ever since the 1500s, when an unknown printer took a galley of type and scrambled it to make a type specimen book. It has survived not only five centuries, but also the leap into electronic typesetting, remaining essentially unchanged. It was popularised in the 1960s with the release of Letraset sheets containing Lorem Ipsum passages, and more recently with desktop publishing software like Aldus PageMaker including versions of Lorem Ipsum.</p>
  </div>

  <article class="abs post" style="top:936px">
    <div class="day">WEDNESDAY, Mar.16.2016</div>
    <div class="ph thumb" role="img" aria-label="Dark fantasy game cover art with a horned demon"></div>
    <div class="abs body">
      <h3>It is a long established fact that a reader will be content of a page when layout.</h3>
      <p>Lorem Ipsum is simply dummy text of the printing and typesetting industry. Lorem Ipsum has been the industry's standard dummy text ever since the 1500s, when an unknown printer took a galley of type and scrambled it to make a type specimen book.</p>
      <div class="tags"><span>Frost Outpost</span><span>Nightline 2</span><span>Pixel Cube Kid</span><span>Front Signal 4</span><span>Emberpath 2</span><span>Blockhaven</span></div>
    </div>
    <div class="abs byline">POSTED BY &nbsp;| <b>ALAN PRYCE</b></div>
  </article>

  <article class="abs post" style="top:1276px">
    <div class="day">WEDNESDAY, Mar.16.2016</div>
    <div class="ph thumb" role="img" aria-label="Dark fantasy game cover art with a horned demon"></div>
    <div class="abs body">
      <h3>It is a long established fact that a reader will be content of a page when layout.</h3>
      <p>Lorem Ipsum is simply dummy text of the printing and typesetting industry. Lorem Ipsum has been the industry's standard dummy text ever since the 1500s, when an unknown printer took a galley of type and scrambled it to make a type specimen book.</p>
      <div class="tags"><span>Frost Outpost</span><span>Nightline 2</span><span>Pixel Cube Kid</span><span>Front Signal 4</span><span>Emberpath 2</span><span>Blockhaven</span></div>
    </div>
    <div class="abs byline">POSTED BY &nbsp;| <b>ALAN PRYCE</b></div>
  </article>

  <article class="abs post" style="top:1616px">
    <div class="day">WEDNESDAY, Mar.16.2016</div>
    <div class="ph thumb" role="img" aria-label="Dark fantasy game cover art with a horned demon"></div>
    <div class="abs body">
      <h3>It is a long established fact that a reader will be content of a page when layout.</h3>
      <p>Lorem Ipsum is simply dummy text of the printing and typesetting industry. Lorem Ipsum has been the industry's standard dummy text ever since the 1500s, when an unknown printer took a galley of type and scrambled it to make a type specimen book.</p>
      <div class="tags"><span>Frost Outpost</span><span>Nightline 2</span><span>Pixel Cube Kid</span><span>Front Signal 4</span><span>Emberpath 2</span><span>Blockhaven</span></div>
    </div>
    <div class="abs byline">POSTED BY &nbsp;| <b>ALAN PRYCE</b></div>
  </article>
</main>

<aside>
  <div class="abs side-head" style="top:680px">Popular</div>
  <div class="abs side-item" style="top:770px">
    <div class="ph pic pic-knight" role="img" aria-label="Armored game character standing"></div>
    <div class="abs txt"><h4>Mar 16, 2016</h4><p>Lorem Ipsum is simply dummy text of the printing and typesetting industry</p></div>
  </div>
  <div class="abs side-item" style="top:925px">
    <div class="ph pic pic-cube" role="img" aria-label="Red cube-shaped game character"></div>
    <div class="abs txt"><h4>Mar 16, 2016</h4><p>Lorem Ipsum is simply dummy text of the printing and typesetting industry</p></div>
  </div>
  <div class="abs more" style="top:1068px">more popular &gt;&gt;</div>

  <div class="abs side-head" style="top:1127px">Blog</div>
  <div class="abs recent">RECENT COMMENTS</div>
  <div class="abs comment" style="top:1253px"><p>Lorem Ipsum is simply dummy text of the printing and typesetting industry</p><time>WED, Mar.16.2016</time></div>
  <div class="abs comment" style="top:1350px"><p>Lorem Ipsum is simply dummy text of the printing and typesetting industry</p><time>WED, Mar.16.2016</time></div>
  <div class="abs more" style="top:1440px;left:742px">more comments &gt;&gt;</div>

  <div class="abs side-head" style="top:1500px">News &amp; Info</div>
  <div class="abs side-item" style="top:1590px">
    <div class="ph pic pic-knight" role="img" aria-label="Armored game character standing"></div>
    <div class="abs txt"><h4>Frost Outpost</h4><p>Lorem Ipsum is simply dummy text of the printing and typesetting industry</p><div class="meta">55 Comments &nbsp; 12 Shares</div></div>
  </div>
  <div class="abs side-item" style="top:1745px">
    <div class="ph pic pic-cube" role="img" aria-label="Red cube-shaped game character"></div>
    <div class="abs txt"><h4>Pixel Cube Kid</h4><p>Lorem Ipsum is simply dummy text of the printing and typesetting industry</p><div class="meta">55 Comments &nbsp; 12 Shares</div></div>
  </div>
  <div class="abs more" style="top:1890px">more news &gt;&gt;</div>
</aside>

<section>
  <div class="ph banner" role="img" aria-label="Small armored knight character with a sword in a dark blue cave"></div>
  <div class="abs banner-text">
    <h2>KIP VIDEO GAMES LOREM LIPSUM</h2>
    <p>It is a long established fact that a reader will be distracted by the readable content of a page when looking at its layout.</p>
    <span class="btn">MORE</span>
  </div>
</section>

<section>
  <div class="abs testimonial"></div>
  <div class="abs quote-mark" style="left:100px;top:2420px">&ldquo;</div>
  <div class="abs quote-mark" style="left:1060px;top:2680px">&rdquo;</div>
  <div class="ph avatar" role="img" aria-label="Portrait photo of the reviewer"></div>
  <blockquote class="abs testimonial-text">
    <p>Lorem Ipsum is simply dummy text of the printing and typesetting industry. Lorem Ipsum has been the industry's standard dummy text ever since the 1500s, when an unknown printer took a galley of type and scrambled it to make a type specimen book.</p>
    <cite>Clara Whitlow</cite>
  </blockquote>
</section>

<footer>
  <div class="abs footer">
    <div class="abs col" style="left:48px">
      <h5>Quick Links</h5>
      <ul><li>Home</li><li>Reviews</li><li>Gallery</li><li>News &amp; Info</li><li>Blog</li></ul>
    </div>
    <div class="abs col contact" style="left:273px">
      <h5>Contact Us</h5>
      <p>Kip Video Games</p>
      <p>2150 Harbor Loop, Ridgeview,<br>NV 89502</p>
      <p class="phone">555-214-0386</p>
      <p>hello@kipvideogames.example</p>
    </div>
    <div class="abs col" style="left:661px">
      <h5>Newsletter</h5>
      <div class="field">Name</div>
      <div class="field">Email</div>
      <div class="subscribe">Subscribe</div>
    </div>
    <div class="abs col" style="left:957px">
      <h5>Social Media</h5>
      <div class="social-foot"><span></span><span></span><span></span><span></span></div>
    </div>
  </div>
  <div class="abs copyright">Copyrights 2016 Kip Video Games Media company. All Rights Reserved.</div>
</footer>

</body>
</html>
```